Refresh of The Marston Collective business card

Update business card design using existing primary logo. Names, numbers, etc. are too hard to read on current design.

Target Market(s)

We are a CPA firm.

Industry/Entity Type

Accountant

Contact Information for Business Card

update current card

Colors
0355a3
3176b5
85acd3
0792cd

Requirements
Must have
• Easier to read phone numbers and names
• Use existing logo
Nice to have
• We love our color scheme and current TMC logo. But the names and phone numbers are too small and card just look old and stale.

```html
<!DOCTYPE html>
<html lang="en">
<head>
<meta charset="utf-8">
<title>The Marston Collective — Business Card</title>
<link href="https://fonts.googleapis.com/css2?family=Didact+Gothic&family=Marcellus+SC&display=swap" rel="stylesheet">
<style>
  :root {
    --brand-blue: #0355a3;
    --brand-blue-deep: #023a78;
    --brand-mid: #3176b5;
    --brand-light: #85acd3;
    --brand-cyan: #0792cd;
    --swoosh-grey: #4a4a4a;
    --paper: #ffffff;
    --stage: #e6e9ec;
  }
  html, body {
    margin: 0;
    padding: 0;
    width: 1200px;
    height: 960px;
    overflow: hidden;
    background: var(--stage);
  }
  .canvas {
    position: relative;
    width: 1200px;
    height: 960px;
  }
  .card {
    position: absolute;
    left: 250px;
    width: 700px;
    height: 400px;
    overflow: hidden;
    box-shadow: 0 6px 18px rgba(0,0,0,0.18);
  }
  .card-front { top: 60px; }
  .card-back {
    top: 500px;
    background: radial-gradient(ellipse at 50% 40%, var(--brand-mid) 0%, var(--brand-blue) 45%, var(--brand-blue-deep) 100%);
  }
  .front-art {
    position: absolute;
    inset: 0;
  }
  .brand {
    position: absolute;
    display: flex;
    align-items: center;
    gap: 14px;
  }
  .brand-disc {
    border-radius: 50%;
    flex: none;
  }
  .brand-name {
    font-family: "Marcellus SC", serif;
    line-height: 1.05;
  }
  .card-front .brand { top: 52px; left: 420px; }
  .card-front .brand-disc {
    width: 62px; height: 62px;
    background: var(--brand-blue);
  }
  .card-front .brand-name {
    font-size: 27px;
    color: var(--brand-blue);
    width: 200px;
  }
  .holder {
    position: absolute;
    left: 58px;
    top: 108px;
    color: var(--paper);
  }
  .holder-name {
    font-family: "Marcellus SC", serif;
    font-size: 32px;
    margin: 0;
    letter-spacing: 0.5px;
  }
  .holder-title {
    font-family: "Marcellus SC", serif;
    font-size: 20px;
    margin: 6px 0 0;
  }
  .address {
    position: absolute;
    left: 58px;
    top: 196px;
    font-family: "Didact Gothic", sans-serif;
    font-size: 19px;
    line-height: 26px;
    color: var(--paper);
    margin: 0;
    font-style: normal;
  }
  .contacts {
    position: absolute;
    left: 58px;
    top: 270px;
    margin: 0;
    padding: 0;
    list-style: none;
    font-family: "Didact Gothic", sans-serif;
    font-size: 19px;
    color: var(--paper);
  }
  .contacts li {
    display: flex;
    align-items: center;
    gap: 12px;
    height: 24.5px;
  }
  .contacts svg {
    width: 15px;
    height: 15px;
    fill: var(--paper);
    flex: none;
  }
  .card-back .brand {
    left: 50%;
    top: 120px;
    transform: translateX(-50%);
  }
  .card-back .brand-disc {
    width: 96px; height: 96px;
    background: var(--paper);
  }
  .card-back .brand-name {
    font-size: 38px;
    color: var(--paper);
    width: 250px;
  }
  .back-web {
    position: absolute;
    left: 0;
    right: 0;
    top: 290px;
    text-align: center;
    font-family: "Didact Gothic", sans-serif;
    font-size: 20px;
    letter-spacing: 1px;
    color: var(--paper);
  }
</style>
</head>
<body>
<main class="canvas">
  <section class="card card-front">
    <svg class="front-art" viewBox="0 0 700 400" width="700" height="400" aria-hidden="true">
      <defs>
        <radialGradient id="frontBlue" cx="30%" cy="35%" r="80%">
          <stop offset="0" stop-color="#3176b5"/>
          <stop offset="0.5" stop-color="#0355a3"/>
          <stop offset="1" stop-color="#023a78"/>
        </radialGradient>
      </defs>
      <rect width="700" height="400" fill="url(#frontBlue)"/>
      <path d="M300 0 C 380 170, 500 330, 700 388 L700 0 Z" fill="#ffffff"/>
      <path d="M352 22 C 420 180, 520 320, 690 384 C 530 330, 420 200, 352 22 Z" fill="#4a4a4a"/>
      <path d="M336 0 C 400 160, 500 300, 700 372 L700 0 Z" fill="#ffffff"/>
    </svg>

    <div class="brand">
      <span class="brand-disc"></span>
      <span class="brand-name">The Marston Collective</span>
    </div>

    <div class="holder">
      <h1 class="holder-name">Daniel R. Marston</h1>
      <p class="holder-title">CPA</p>
    </div>

    <address class="address">318 E. Holloway Ave. Suite 112<br>Brookhaven, Florida 32700</address>

    <ul class="contacts">
      <li><svg viewBox="0 0 16 16"><path d="M3 1l3 3-1.5 2a9 9 0 0 0 5.5 5.5L12 10l3 3-2 2C7 15 1 9 1 3z"/></svg>407.555.0142</li>
      <li><svg viewBox="0 0 16 16"><path d="M4 1h8v4H4zM1 6h14v6h-3v3H4v-3H1zM5 10v4h6v-4z"/></svg>407.555.0187</li>
      <li><svg viewBox="0 0 16 16"><path d="M4 0h8v16H4zM5.5 2v9h5V2zM7 13h2v1.5H7z"/></svg>407.555.0163</li>
      <li><svg viewBox="0 0 16 16"><path d="M1 3h14v10H1zM2.5 4.5L8 9l5.5-4.5z"/></svg>dan@themarstoncollective.com</li>
      <li><svg viewBox="0 0 16 16"><path d="M8 1a7 7 0 1 0 0 14A7 7 0 0 0 8 1zm0 1.5c.8 0 1.8 1.9 2 4.7H6c.2-2.8 1.2-4.7 2-4.7zM2.6 7.2h2.1c.1-1.7.5-3.2 1-4.1a5.6 5.6 0 0 0-3.1 4.1zm8.7 0h2.1a5.6 5.6 0 0 0-3.1-4.1c.5.9.9 2.4 1 4.1zM2.6 8.8a5.6 5.6 0 0 0 3.1 4.1c-.5-.9-.9-2.4-1-4.1zm3.4 0c.2 2.8 1.2 4.7 2 4.7s1.8-1.9 2-4.7zm5.3 0c-.1 1.7-.5 3.2-1 4.1a5.6 5.6 0 0 0 3.1-4.1z"/></svg>www.themarstoncollective.com</li>
    </ul>
  </section>

  <section class="card card-back">
    <div class="brand">
      <span class="brand-disc"></span>
      <span class="brand-name">The Marston Collective</span>
    </div>
    <p class="back-web">www.themarstoncollective.com</p>
  </section>
</main>
</body>
</html>
```